Basisdesign Buch-/E-Book-Cover für Haldmoor-Krimis
Zielgruppe
Ich schreibe Krimis, Thriller, Kriminalstories, Krimiparodien.
Meine Zielgruppe sind deutschsprachige Krimi-Leser.
Aufgabenstellung
Ich benötige ein Basisdesign für Buchcover (Höhe 2.343, Breite 1.518 Pixel – Druckfalter, eBooks). Alle Bücher haben mit Crime zu tun, aber in verschiedenen Unter-Genres: Klassischer Kriminalroman, Thriller, Fantasy Thriller, Kurzgeschichten, Krimi-Parodien.
Ich benötige, quasi als Marke, dafür ein gleichbleibendes grafisches Element, z. B. einen Sockel im unteren Coverbereich, der den Autorennamen „Jonas Haldmoor“ und das jeweilige Unter-Genre enthält. Unter-Genres sind: Krimi, Thriller, Fantasy-Thriller, Kurzgeschichten und Krimi-Parodie. Das alles sollte auch noch im Format der Lesoria-Bücherlisten wie „Kunden kauften auch“ halbwegs lesbar sein.
Ein bisschen mörderisch und blutig sind alle Varianten.
Nachdem die Bandbreite vom Thriller bis zur Parodie reicht, sollte der gleichbleibende Markenbereich eine entsprechende grafische Bandbreite aufweisen, dabei aber die Grundmelodie Crime nicht aus den Augen verlieren.
Im oberen Bereich stelle ich mir Grafiken oder Hintergrundfotos vor, die für jedes Buch individuell gestaltet werden müssten, was jedoch über das Basisdesign hinausgeht. Die Wahl der Schriftart für Titel (bislang 11 – 25 Zeichen inkl. Leerzeichen) und allfällige Untertitel (im Umfang von maximal 30 Zeichen), sollte zu denen im Sockel passen.

```html
<!DOCTYPE html>
<html lang="de">
<head>
<meta charset="utf-8">
<title>Hang des Todes – Jonas Haldmoor</title>
<link rel="stylesheet" href="https://fonts.googleapis.com/css2?family=Bebas+Neue&family=Playfair+Display:ital,wght@0,400;1,400&display=swap">
<style>
  :root {
    --sky-top: #cfe0ea;
    --sky-mid: #9fbfd6;
    --mountain: #4f6f86;
    --valley-green: #6f8f52;
    --meadow: #a7be86;
    --blood: #d91318;
    --band-red: #e01218;
    --paper: #f6f4ef;
    --ink: #1a1112;
    --knife: #5a1011;
    --white: #ffffff;
  }
  * { margin: 0; padding: 0; box-sizing: border-box; }
  html, body { width: 768px; height: 1200px; overflow: hidden; background: var(--white); }
  .cover {
    position: relative;
    width: 768px;
    height: 1200px;
    overflow: hidden;
  }
  .cover-photo {
    position: absolute;
    inset: 0 0 330px 0;
    background: linear-gradient(180deg, var(--sky-top) 0%, var(--sky-mid) 35%, var(--mountain) 62%, var(--valley-green) 88%, #89a866 100%);
  }
  .meadow-photo {
    position: absolute;
    left: 0; right: 0; bottom: 0;
    height: 110px;
    background: linear-gradient(180deg, #c9d8b4 0%, var(--meadow) 50%, #8eab6a 100%);
  }
  .title {
    font-family: "Bebas Neue", "Oswald", sans-serif;
    font-weight: 400;
    color: var(--blood);
  }
  .title-line {
    position: absolute;
    left: 0; right: 0;
    display: block;
    text-align: center;
    line-height: 1;
    white-space: nowrap;
  }
  .title-line--first { top: 45px; font-size: 268px; letter-spacing: 6px; }
  .title-line--middle { top: 298px; font-size: 192px; letter-spacing: 4px; }
  .title-line--last { top: 508px; font-size: 240px; letter-spacing: 10px; }
  .brand-base {
    position: absolute;
    left: 0; top: 0;
    width: 768px; height: 1200px;
  }
  .subgenre {
    position: absolute;
    left: 0; right: 0; top: 889px;
    text-align: center;
    font-family: "Playfair Display", serif;
    font-style: italic;
    font-size: 39px;
    line-height: 1.2;
    letter-spacing: 1px;
    color: var(--ink);
  }
  .knife {
    position: absolute;
    left: 620px; top: 860px;
    width: 15px; height: 155px;
    transform: rotate(45deg);
    border-radius: 3px;
    background: linear-gradient(180deg, #3c0a0b 0%, var(--knife) 100%);
  }
  .author {
    position: absolute;
    left: 0; right: 0; top: 974px;
    text-align: center;
    font-family: "Playfair Display", serif;
    font-size: 82px;
    line-height: 1;
    color: var(--white);
    white-space: nowrap;
  }
</style>
</head>
<body>
<main class="cover">
  <div class="cover-photo" role="img" aria-label="Hintergrundfoto: Alpental in Kärnten mit Bergen und Dorfkirche"></div>
  <div class="meadow-photo" role="img" aria-label="Foto einer grünen Bergwiese"></div>

  <h1 class="title">
    <span class="title-line title-line--first">HANG</span>
    <span class="title-line title-line--middle">DES</span>
    <span class="title-line title-line--last">TODES</span>
  </h1>

  <svg class="brand-base" viewBox="0 0 768 1200" aria-hidden="true">
    <polygon fill="var(--paper)" points="0,830 30,822 58,834 92,818 130,830 170,820 210,836 250,824 300,832 340,818 380,830 430,822 470,834 520,820 560,830 600,818 650,832 700,822 740,830 768,820 768,860 0,860"/>
    <polygon fill="var(--band-red)" points="0,846 40,840 80,850 120,838 160,848 200,842 240,852 290,840 330,850 370,842 420,852 460,840 500,848 550,842 590,852 630,840 680,850 720,842 768,848 768,1100 0,1100"/>
    <polygon fill="var(--paper)" points="0,1096 40,1104 80,1094 130,1106 170,1098 220,1108 260,1096 310,1104 350,1094 400,1106 440,1098 490,1108 530,1096 580,1104 620,1094 670,1106 710,1098 768,1104 768,1118 720,1112 680,1122 630,1110 580,1120 530,1112 480,1122 430,1110 380,1120 330,1112 280,1122 230,1110 180,1120 130,1112 80,1122 40,1110 0,1118"/>
  </svg>

  <p class="subgenre">Ein Kärnten-Thriller</p>
  <div class="knife" role="img" aria-label="Illustration eines Küchenmessers"></div>
  <p class="author">Jonas Haldmoor</p>
</main>
</body>
</html>
```